Thrifty Haul: Junk Removal - Website Design

We need a design and uploaded to Hostplume.com. I enclosed our postcard for reference too. I need a contact from at the top right so I can get leads.

Here are the sites I like:

https://carrybrisk.example/
https://www.1800tossbin.example
https://www.campusmoverscleardebris.example/junk-removal/
http://aroomfornanas.example/
http://www.driftwhirl.example/alternate/
https://www.servicemenautogifts.example/
http://www.wheelsforsoldiers.example/indexj/

```html
<!DOCTYPE html>
<html lang="en">
<head>
<meta charset="utf-8">
<title>Thrifty Haul – Junk Removal</title>
<link rel="stylesheet" href="https://fonts.googleapis.com/css2?family=Bebas+Neue&family=Open+Sans:ital,wght@0,400;0,600;0,700;1,400&display=swap">
<style>
:root{
  --green:#7dbb20;
  --blue:#10479b;
  --navy:#1b2738;
  --navy-dark:#152030;
  --text:#333;
  --muted:#555;
  --light:#f1f1f1;
  --white:#fff;
}
*{box-sizing:border-box;margin:0;padding:0}
html,body{width:1200px;height:4157px;overflow:hidden}
body{position:relative;background:#fff;font-family:"Open Sans",sans-serif;color:var(--text)}
.abs{position:absolute}
.display{font-family:"Bebas Neue",sans-serif;font-weight:400;letter-spacing:.5px;line-height:1}
.g{color:var(--green)} .b{color:var(--blue)}
.brand{font-family:"Bebas Neue",sans-serif;color:var(--green);line-height:1}

/* header */
.topbar{top:0;left:0;width:1200px;height:112px;background:#fff}
.icon-circle{border-radius:50%;background:var(--blue);display:flex;align-items:center;justify-content:center}
.top-label{font-size:15px;color:#555;font-weight:600}
.top-value{font-family:"Bebas Neue",sans-serif;font-size:32px;color:var(--blue)}
.nav{top:112px;left:0;width:1200px;height:62px;background:var(--green)}
.nav a{position:absolute;top:21px;color:#fff;font-size:16px;text-decoration:none}

/* hero */
.hero-title{left:51px;top:255px;font-size:56px}
.hero-sub{left:51px;top:380px;font-size:21px;font-weight:600;color:#555}
.btn{background:var(--green);color:#fff;display:flex;align-items:center;justify-content:center;text-decoration:none}
.quote-panel{left:795px;top:97px;width:363px;height:493px;background:var(--blue)}
.quote-panel h2{position:absolute;top:20px;left:0;width:100%;text-align:center;color:#fff;font-size:24px;font-weight:700;line-height:1.35}
.field{position:absolute;left:32px;width:294px;height:62px;background:#fff;border:1px solid #ccd}
.field .lbl{position:absolute;left:36px;top:10px;font-size:12px;color:var(--blue)}
.field .ph{position:absolute;left:12px;top:34px;font-size:13px;color:#777}

/* features */
.feat-circle{width:86px;height:86px;border-radius:50%;background:#e8e8e8;display:flex;align-items:center;justify-content:center}
.feat-label{font-size:26px;color:#444}

/* services */
.check-list{font-size:17px;color:#444;line-height:32px}
.check-list span{color:var(--green);margin-right:8px}
.card{top:1487px;width:238px;height:265px;background:#fff;box-shadow:0 2px 6px rgba(0,0,0,.15);text-align:center}
.card .ic{width:124px;height:124px;border-radius:50%;background:#e8e8e8;margin:34px auto 0;display:flex;align-items:center;justify-content:center}
.card p{margin-top:22px;font-size:20px;font-weight:700;color:#222;line-height:1.35}

/* footer */
.footer{top:3607px;left:0;width:1200px;height:448px;background:var(--navy)}
.foot-bottom{top:4055px;left:0;width:1200px;height:102px;background:var(--navy-dark);color:#fff;font-size:12px;text-align:center;line-height:102px}
.foot-h{font-size:20px;font-weight:700;color:#fff}
.foot-menu{color:#ddd;font-size:20px;line-height:44px;list-style:none}
.foot-menu li span{color:#d63a3a;font-size:14px;margin-right:18px}
.social{width:48px;height:48px;border-radius:50%;border:1px solid #8a93a3}
</style>
</head>
<body>

<!-- header -->
<header class="abs topbar">
  <div class="abs brand" style="left:85px;top:28px;font-size:54px">Thrifty Haul</div>
  <div class="abs icon-circle" style="left:560px;top:24px;width:58px;height:58px">
    <svg width="28" height="28" viewBox="0 0 24 24" fill="none" stroke="#fff" stroke-width="1.6"><circle cx="12" cy="12" r="10"/><path d="M2 12h20M12 2c3 3 3 17 0 20M12 2c-3 3-3 17 0 20"/></svg>
  </div>
  <div class="abs top-label" style="left:628px;top:22px">Your Location</div>
  <div class="abs" style="left:628px;top:50px;width:32px;height:22px;background:linear-gradient(#c33 0 15%,#fff 15% 30%,#c33 30% 45%,#fff 45% 60%,#c33 60% 75%,#fff 75% 90%,#c33 90%)"></div>
  <div class="abs top-value" style="left:672px;top:46px">USA <span style="font-size:20px">&#8964;</span></div>
  <div class="abs icon-circle" style="left:848px;top:22px;width:60px;height:60px">
    <svg width="28" height="28" viewBox="0 0 24 24" fill="none" stroke="#fff" stroke-width="1.8"><path d="M5 3h4l2 5-2.5 1.5a11 11 0 005 5L15 12l5 2v4a2 2 0 01-2 2A16 16 0 013 5a2 2 0 012-2z"/></svg>
  </div>
  <div class="abs top-label" style="left:917px;top:22px">24/7 Customer Service</div>
  <div class="abs top-value" style="left:917px;top:44px;font-size:36px">1-800-555-0148</div>
</header>

<nav class="abs nav">
  <a style="left:88px">Home</a><a style="left:176px">What We Do</a><a style="left:312px">About Us</a><a style="left:423px">Contact Us</a><a style="left:547px">Book Online</a>
</nav>

<!-- hero -->
<svg class="abs" style="left:0;top:174px" width="1200" height="391">
  <polygon points="640,391 800,180 800,0 1200,0 1200,391" fill="var(--green)"/>
  <polygon points="770,0 1200,0 1200,60" fill="var(--green)"/>
</svg>
<div class="abs display hero-title g">No Contact<br><span class="b">Junk Removal</span></div>
<div class="abs hero-sub">All You Have To Do Is Point</div>
<a class="abs btn" style="left:51px;top:434px;width:157px;height:43px;font-size:16px">Learn More</a>
<div class="abs" role="img" aria-label="Box truck with two uniformed workers holding brooms" style="left:400px;top:240px;width:395px;height:250px;background:linear-gradient(135deg,#e4e8ee,#1d3c7a 70%);border-radius:6px"></div>

<section class="abs quote-panel">
  <svg class="abs" style="left:-28px;top:0" width="30" height="20"><polygon points="28,0 28,18 0,18" fill="var(--blue)"/></svg>
  <h2>Get Free Quotes from<br>Our Specialists!</h2>
  <div class="field" style="top:115px"><span class="lbl">Name</span><span class="ph">Enter Your Full Name</span></div>
  <div class="field" style="top:189px"><span class="lbl">Email</span><span class="ph">Enter Your Email Address</span></div>
  <div class="field" style="top:265px"><span class="lbl">Phone</span><span class="ph">Enter Your Phone Number</span></div>
  <div class="field" style="top:340px"><span class="lbl">State</span><span class="ph">Select Your State</span><span class="abs" style="right:18px;top:14px;color:var(--blue);font-size:24px">&#8964;</span></div>
  <div class="btn" style="position:absolute;left:32px;top:416px;width:294px;height:43px;font-size:16px">Get Quote Now</div>
</section>

<!-- about -->
<div class="abs" style="left:0;top:565px;width:1200px;height:628px;background:#f8f8f8"></div>
<svg class="abs" style="left:0;top:565px" width="640" height="628" role="img" aria-label="Two movers in purple shirts handing a cardboard box">
  <defs><linearGradient id="ph1" x1="0" y1="0" x2="1" y2="1"><stop offset="0" stop-color="#c9a27a"/><stop offset=".5" stop-color="#6b3aa8"/><stop offset="1" stop-color="#4a4a52"/></linearGradient></defs>
  <polygon points="0,0 620,0 210,628 0,628" fill="url(#ph1)"/>
</svg>
<div class="abs display" style="left:648px;top:645px;font-size:52px"><span class="g">Full Service</span> <span class="b">Junk Removal</span></div>
<p class="abs" style="left:610px;top:725px;width:520px;font-size:18px;line-height:26px;color:#444">Thrifty Haul is full-service junk removal company serving areas across the United States. We're in your neighborhood.</p>
<div class="abs display" style="left:500px;top:868px;font-size:38px"><span class="g">Why</span> <span class="b">Thrifty Haul</span></div>

<div class="abs feat-circle" style="left:430px;top:940px"><svg width="44" height="44" viewBox="0 0 24 24" fill="none" stroke="var(--blue)" stroke-width="1.4"><circle cx="13" cy="12" r="8"/><path d="M13 7v5l3 2M2 9h4M1 12h4M2 15h4"/></svg></div>
<div class="abs feat-label" style="left:534px;top:966px">On-time Service</div>
<div class="abs feat-circle" style="left:790px;top:940px"><svg width="44" height="44" viewBox="0 0 24 24" fill="none" stroke="var(--blue)" stroke-width="1.4"><ellipse cx="9" cy="6" rx="5" ry="2"/><path d="M4 6v10c0 1 2 2 5 2M14 6v4"/><circle cx="16" cy="15" r="5"/><path d="M16 12v6"/></svg></div>
<div class="abs feat-label" style="left:894px;top:966px">Up Front Pricing</div>
<div class="abs feat-circle" style="left:355px;top:1057px"><svg width="44" height="44" viewBox="0 0 24 24" fill="none" stroke="var(--blue)" stroke-width="1.4"><circle cx="12" cy="12" r="6"/><path d="M12 2v4M12 18v4M2 12h4M18 12h4M5 5l3 3M16 16l3 3M19 5l-3 3M8 16l-3 3"/></svg></div>
<div class="abs feat-label" style="left:460px;top:1083px">Covid-19 Compliant</div>
<div class="abs feat-circle" style="left:735px;top:1057px"><svg width="44" height="44" viewBox="0 0 24 24" fill="none" stroke="var(--blue)" stroke-width="1.4"><path d="M5 5h14l-2 16H7z M4 5h16"/><path d="M10 13l2-3 2 3-2 3z"/></svg></div>
<div class="abs feat-label" style="left:840px;top:1083px">Full Service Junk Removal</div>

<!-- services -->
<div class="abs" style="left:0;top:1193px;width:1200px;height:629px;background:#eeeeee"></div>
<svg class="abs" style="left:0;top:1193px" width="1200" height="629" role="img" aria-label="Blue garbage truck at a collection site">
  <defs><linearGradient id="ph2" x1="0" y1="0" x2="1" y2="1"><stop offset="0" stop-color="#3f6fb8"/><stop offset=".6" stop-color="#1d4a94"/><stop offset="1" stop-color="#2f3744"/></linearGradient></defs>
  <polygon points="790,0 1200,0 1200,629 365,629" fill="url(#ph2)"/>
</svg>
<div class="abs display" style="left:89px;top:1270px;font-size:40px"><span class="g">What</span> <span class="b">We Do</span></div>
<div class="abs check-list" style="left:89px;top:1361px"><span>&#10003;</span>Residental<br><span>&#10003;</span>Storage</div>
<div class="abs check-list" style="left:236px;top:1361px"><span>&#10003;</span>Moving<br><span>&#10003;</span>Disasters</div>
<div class="abs check-list" style="left:373px;top:1361px"><span>&#10003;</span>Commercial Junk Removal<br><span>&#10003;</span>Renovation</div>

<div class="abs card" style="left:91px"><div class="ic"><svg width="70" height="70" viewBox="0 0 24 24" fill="none" stroke="var(--blue)" stroke-width="1.2"><path d="M4 7h10l-1 13H5z"/><path d="M15 12h5v8h-5z" fill="var(--green)" stroke="var(--green)"/></svg></div><p>House, Garage,<br>Estate Clean Out</p></div>
<div class="abs card" style="left:352px"><div class="ic"><svg width="70" height="70" viewBox="0 0 24 24" fill="none" stroke="var(--blue)" stroke-width="1.2"><rect x="3" y="3" width="8" height="18"/><path d="M3 10h8"/><rect x="13" y="9" width="8" height="12" fill="var(--green)" stroke="var(--green)"/><circle cx="17" cy="15" r="2.5" stroke="#fff"/></svg></div><p>Furniture,<br>Appliance Removal</p></div>
<div class="abs card" style="left:613px"><div class="ic"><svg width="70" height="70" viewBox="0 0 24 24" fill="none" stroke="var(--blue)" stroke-width="1.2"><rect x="8" y="3" width="8" height="18"/><path d="M10 6h4M10 9h4M10 12h4M10 15h4"/><rect x="3" y="13" width="4" height="8" fill="var(--green)" stroke="var(--green)"/><rect x="17" y="11" width="4" height="10" fill="var(--green)" stroke="var(--green)"/><path d="M1 21h22"/></svg></div><p>Commercial<br>Junk Removal</p></div>
<div class="abs card" style="left:875px"><div class="ic"><svg width="70" height="70" viewBox="0 0 24 24" fill="none" stroke="var(--blue)" stroke-width="1.2"><rect x="3" y="11" width="6" height="9"/><rect x="9" y="11" width="6" height="9"/><rect x="15" y="11" width="6" height="9" fill="var(--green)" stroke="var(--green)"/><path d="M12 3v5M10 5l2-2 2 2"/></svg></div><p>We<br>Recycle</p></div>

<!-- locator -->
<div class="abs" style="left:0;top:1822px;width:1200px;height:700px;background:#f9f9f9"></div>
<div class="abs" role="img" aria-label="Map of the United States" style="left:595px;top:1945px;width:605px;height:455px;background:#fbdccb;border-radius:40px 0 0 120px"></div>
<div class="abs b" style="left:88px;top:2000px;font-size:30px">America's Most Trusted Name in</div>
<div class="abs display g" style="left:88px;top:2050px;font-size:64px">Junk Removal</div>
<div class="abs" style="left:88px;top:2140px;font-size:32px;line-height:42px;color:#555">Find Our Junk Removal Service In<br>Your Area</div>
<div class="abs" style="left:88px;top:2270px;width:512px;height:85px;border:1px solid #999;background:#fff"></div>
<div class="abs" style="left:118px;top:2300px;font-size:20px;color:#666">Enter Your Zip Code</div>
<div class="abs btn" style="left:515px;top:2270px;width:85px;height:85px"><svg width="30" height="34" viewBox="0 0 24 24" fill="#fff"><path d="M12 2a7 7 0 00-7 7c0 5 7 13 7 13s7-8 7-13a7 7 0 00-7-7zm0 10a3 3 0 110-6 3 3 0 010 6z"/></svg></div>

<!-- testimonials -->
<svg class="abs" style="left:0;top:2522px" width="1200" height="590" role="img" aria-label="Movers loading a vehicle, tinted blue">
  <rect width="1200" height="590" fill="var(--green)"/>
  <polygon points="562,0 1200,0 1200,575 175,590" fill="#1a4a98"/>
  <circle cx="300" cy="308" r="157" fill="none" stroke="#fff" stroke-width="1.5" stroke-dasharray="6 6"/>
  <circle cx="335" cy="308" r="93" fill="#c79a7a"/>
  <circle cx="310" cy="162" r="22" fill="#d9d9d9"/>
  <circle cx="197" cy="233" r="20" fill="#d9d9d9"/>
  <circle cx="187" cy="389" r="20" fill="#d9d9d9"/>
  <circle cx="487" cy="265" r="26" fill="#6b3aee"/>
  <text x="487" y="277" font-family="Bebas Neue, sans-serif" font-size="34" fill="#fff" text-anchor="middle">&#8220;</text>
</svg>
<div class="abs display" style="left:585px;top:2640px;font-size:36px;color:#fff"><span class="g">What</span> Our Customers Say</div>
<p class="abs" style="left:548px;top:2767px;width:500px;font-size:14px;font-style:italic;line-height:20px;color:#fff">" Lorem ipsum dolor sit amet, consectetur adipiscing elit, sed do eiusmod tempor incididunt ut labore et dolore magna aliqua. Ut enim ad minim veniam, quis nostrud exercitation ullamco laboris nisi ut aliquip ex ea commodo consequat. velit esse cillum fugiat nulla pariatur. "</p>
<div class="abs g" style="left:548px;top:2878px;font-size:12px">Marla Quentin</div>
<div class="abs g" style="left:680px;top:2876px;font-size:12px;letter-spacing:1px">&#9733;&#9733;&#9733;&#9733;&#9733;</div>
<div class="abs btn" style="left:549px;top:2935px;width:36px;height:36px;border-radius:50%">&#8592;</div>
<div class="abs btn" style="left:597px;top:2935px;width:36px;height:36px;border-radius:50%">&#8594;</div>

<!-- call to action -->
<div class="abs" style="left:0;top:3112px;width:1200px;height:495px;background:#f1f1f1"></div>
<div class="abs display b" style="left:0;top:3185px;width:1200px;text-align:center;font-size:84px">Get your <span class="g">junk</span> removed today.</div>
<div class="abs btn" style="left:337px;top:3302px;width:110px;height:110px;border-radius:50%;border:5px solid #fff;box-shadow:0 0 0 1px #ddd">
  <svg width="44" height="44" viewBox="0 0 24 24" fill="none" stroke="#fff" stroke-width="1.8"><path d="M5 3h4l2 5-2.5 1.5a11 11 0 005 5L15 12l5 2v4a2 2 0 01-2 2A16 16 0 013 5a2 2 0 012-2z"/></svg>
</div>
<div class="abs b" style="left:465px;top:3314px;font-size:21px;font-weight:700">Talk Today to a Local Advisor for FREE</div>
<div class="abs display b" style="left:465px;top:3348px;font-size:72px">1-800-555-0148</div>
<a class="abs btn" style="left:491px;top:3467px;width:219px;height:73px;font-size:20px;font-weight:700">Book Online</a>

<!-- footer -->
<footer class="abs footer">
  <div class="abs brand" style="left:126px;top:90px;font-size:52px">Thrifty Haul</div>
  <p class="abs" style="left:126px;top:168px;width:270px;font-size:15px;line-height:26px;color:#ddd">Thrifty Haul is full-service junk removal company serving areas across the United States. We're in your neighborhood.</p>
  <div class="abs social" style="left:126px;top:304px"></div>
  <div class="abs social" style="left:183px;top:304px"></div>
  <div class="abs social" style="left:239px;top:304px"></div>
  <div class="abs social" style="left:296px;top:304px"></div>
  <div class="abs foot-h" style="left:558px;top:100px">Quick Menu</div>
  <ul class="abs foot-menu" style="left:560px;top:171px">
    <li><span>&#10003;</span>About Us</li><li><span>&#10003;</span>Services</li><li><span>&#10003;</span>Blog</li><li><span>&#10003;</span>Contact</li>
  </ul>
  <div class="abs foot-h" style="left:854px;top:100px">Get in Touch</div>
  <svg class="abs" style="left:852px;top:178px" width="24" height="28" viewBox="0 0 24 24" fill="none" stroke="var(--green)" stroke-width="1.6"><path d="M12 2a7 7 0 00-7 7c0 5 7 13 7 13s7-8 7-13a7 7 0 00-7-7z"/><circle cx="12" cy="9" r="2.5"/></svg>
  <p class="abs" style="left:894px;top:178px;font-size:14px;line-height:20px;color:#ddd">Lorem ipsum dolor sit amet,<br>quo te case facete tamquam.</p>
  <svg class="abs" style="left:852px;top:250px" width="24" height="24" viewBox="0 0 24 24" fill="none" stroke="var(--green)" stroke-width="1.6"><path d="M5 3h4l2 5-2.5 1.5a11 11 0 005 5L15 12l5 2v4a2 2 0 01-2 2A16 16 0 013 5a2 2 0 012-2z"/></svg>
  <p class="abs" style="left:894px;top:246px;font-size:14px;line-height:20px;color:#ddd">(888) 555 0188<br>(888) 555 0199</p>
  <svg class="abs" style="left:852px;top:312px" width="24" height="20" viewBox="0 0 24 20" fill="none" stroke="var(--green)" stroke-width="1.6"><rect x="2" y="2" width="20" height="15"/><path d="M2 2l10 8 10-8"/></svg>
  <p class="abs" style="left:894px;top:312px;font-size:14px;color:#ddd">hello@thriftyhaul.example</p>
</footer>
<div class="abs foot-bottom">Copyright © 2020 Company. All rights reserved.</div>

</body>
</html>
```